Business Card Design

Brambledown Pantry is the name of my health coaching business. My tag line is "Where good food meets everyday life." I will be working with clients one-on-one and in groups. My target clients are women "of a certain age" who want to be more comfortable in their own skin. We will work together in a 6-month program. The coaching sessions will take place in my kitchen. I will also be conducting monthly cooking classes and field trips - to farmer's markets, speciality markets etc.. for my clients.
Updates

the business name is Brambledown Pantry - I'm not sure how the p got in there at the end of the name

Thank you

Please include the website - www.brambledownpantry-example.com and the tag line:

Where good food meets everyday life on the business card.

Thank you

Please add the phone number to the business card - sorry, I forgot to state that in the original brief

(555) 274-8150

Target Market(s)

Women "of a certain age" who want to be more comfortable in their own skin

Industry/Entity Type

Cooking

Contact Information for Business Card

Brambledown Pantry
Where good food meets everyday life

Rosalind Hartwell
Health Coach
(555) 274-8150

Font styles to use
Serif
Sans Serif

Requirements
Must have
• front & back design
I typical like soft colors - and have tended toward greens over time - I'm open although I would not like bright reds, yellows etc..

```html
<!DOCTYPE html>
<html lang="en">
<head>
<meta charset="utf-8">
<title>Brambledown Pantry — Business Card</title>
<link rel="stylesheet" href="https://fonts.googleapis.com/css2?family=Arimo:wght@400&family=Roboto+Condensed:wght@300&display=swap">
<style>
  :root {
    --olive: #605e4d;
    --olive-text: #5f604b;
    --ink: #000000;
    --cyan: #14eeee;
    --paper: #ffffff;
    --tagline: #f0f0ec;
  }
  html, body {
    margin: 0;
    padding: 0;
    width: 1200px;
    height: 713px;
    overflow: hidden;
    background: var(--paper);
  }
  .card {
    position: relative;
    width: 1200px;
    height: 713px;
    background: var(--paper);
    font-family: "Arimo", Arial, sans-serif;
  }
  .card-frame {
    position: absolute;
    left: 0;
    top: 0;
  }
  .holder-name {
    position: absolute;
    left: 129px;
    top: 114px;
    margin: 0;
    font-size: 55px;
    font-weight: 400;
    line-height: 1;
    color: var(--olive-text);
    white-space: nowrap;
  }
  .holder-role {
    position: absolute;
    left: 208px;
    top: 196px;
    margin: 0;
    font-size: 43px;
    font-weight: 400;
    line-height: 1;
    color: var(--ink);
    white-space: nowrap;
  }
  .business-name {
    position: absolute;
    left: 386px;
    top: 346px;
    margin: 0;
    font-family: "Roboto Condensed", "Arial Narrow", sans-serif;
    font-weight: 300;
    font-size: 70px;
    line-height: 1;
    color: var(--olive-text);
    white-space: nowrap;
  }
  .contact {
    position: absolute;
    left: 386px;
    top: 431px;
    margin: 0;
    padding: 0;
    list-style: none;
    font-size: 34px;
    line-height: 39px;
    color: var(--cyan);
    white-space: nowrap;
  }
  .tagline {
    position: absolute;
    left: 45px;
    top: 585px;
    width: 1114px;
    height: 74px;
    margin: 0;
    display: flex;
    align-items: center;
    justify-content: center;
    font-size: 46px;
    line-height: 1;
    color: var(--tagline);
    white-space: nowrap;
  }
</style>
</head>
<body>
  <div class="card">
    <svg class="card-frame" width="1200" height="713" viewBox="0 0 1200 713" aria-hidden="true">
      <rect x="45" y="27" width="1114" height="660" fill="none" stroke="var(--olive)" stroke-width="3.5"/>
      <rect x="45" y="585" width="1114" height="74" fill="var(--olive)"/>
    </svg>

    <h1 class="holder-name">Rosalind Hartwell</h1>
    <p class="holder-role">Health Coach</p>

    <h2 class="business-name">BRAMBLEDOWN PANTRY</h2>
    <ul class="contact">
      <li class="contact-phone">Phone : (555) 274-8150</li>
      <li class="contact-email">rosalind@brambledownpantry-example.com</li>
      <li class="contact-web">www.brambledownpantry-example.com</li>
    </ul>

    <p class="tagline">“Where good food meets everyday life”</p>
  </div>
</body>
</html>
```